Wordpress design for my private practice website - Psychotherapist

I would like a simple, clean, and elegant design for my private practice website. I work with both adults and children so I'd like it to appeal to both. However, since parents make the choice as to where to send their child for therapy, I want it to appeal to adults more. I would like the pictures on the site to have a calming effect - maybe using sand and water and rocks. I am attaching files with my company logo. I would also like my name incorporated into the header - Rosalind Vantreece, LCSW, Registered Play Therapist. I've also uploaded a picture of myself for my About Page.

I like the design of these 2 website and want something similar:
www.drmaribelostrand.com
www.harrowgate-lisk.com

I would like a home page that highlights a calming graphic across the entire top of the page as well as my practice logo and my name.

I'd like a link to social media sites on the top of the homepage - facebook, pinterest.

I want a simple bar across the top with the following tabs:
Home
About Me (subtabs Who I Am, Specialties and Approach)
Counseling Services (subtabs Individual Counseling, Play Therapy, Sandplay Therapy,)
Fees
FAQs
Contact Me (would love this to be a fill in the blank contact form that sends info to my email address - should include name, phone number, email and a comment box for more information requested)
Blog (this will link with another wordpress blog)

Target Market(s)

Parents of children under age 12 with behavioral problems or are dealing with the breakup of their family through divorce - looking for someone to work with their young child. I also work with Adults that are overwhelmed and worried - often women that have many life stressors and are feeling burnt out on life and meeting everyone's needs. Families going through some type of trauma, including divorce or grief work. I also work with individuals going through a transition of religious beliefs - often exiting the religion of their youth and undergoing a crisis of faith at midlife.

Industry/Entity Type

Mental Health

Contact Information for Business Card

Rosalind Vantreece, LCSW
Registered Play Therapist
4815 Bellhaven Court
Idaho Falls, Idaho 83404
(208)555-7162
www.stillbrookwellness.com

On the opposite side, I'd like an appointment reminder area - with the following text:

Your next appointment is
_____/______/______ at ______am/pm
Please give 24 hrs notice if you need to cancel your appointment.

Coding

Coded - Design and coding required

Number of Pages Required

5+ page

Font styles to use
Sans Serif

Colors
33a6d7
9bcb3c
0355a3

Requirements
Must have
• I'd like it to be a wordpress site. I'm such a newby at web design - but I need to be able to add content and manage the site myself once it is up and running.
Nice to have
• I like the design of these 2 websites and want something similar:
• www.drmaribelostrand.com
• www.harrowgate-lisk.com
• They are clean, easy to navigate and calming.
Should not have
• Should not look like a childcare website.

```html
<!DOCTYPE html>
<html lang="en">
<head>
<meta charset="utf-8">
<title>Rosalind Vantreece – Stillbrook Wellness</title>
<link href="https://fonts.googleapis.com/css2?family=Dancing+Script:wght@600&family=Josefin+Sans:wght@300;400&family=Roboto:wght@400;500&family=Neuton:wght@400&family=Noto+Serif:wght@400&display=swap" rel="stylesheet">
<style>
  :root{
    --sky:#33a6d7;
    --lime:#c6f04e;
    --nav:#235985;
    --paper:#f5f5f5;
    --ink:#2a2a2a;
    --footer:#6f8a22;
    --footer-dark:#2d3811;
    --footer-head:#d9e9a6;
    --footer-link:#d6f07a;
    --white:#ffffff;
  }
  *{box-sizing:border-box;margin:0;padding:0}
  html,body{width:816px;height:1200px;overflow:hidden;background:var(--white)}
  .page{position:relative;width:816px;height:1200px;overflow:hidden;font-family:"Roboto",sans-serif}

  .hero{position:absolute;left:0;top:0;width:816px;height:349px;
    background:linear-gradient(180deg,#fbfcfd 0%,#f0f3f6 16%,#c9d2dc 30%,#8e9aab 48%,#5e6a7e 68%,#414b5e 100%)}
  .social-top{position:absolute;top:14px;right:43px;display:flex;gap:6px}
  .social-dot{width:24px;height:24px;border-radius:50%;background:var(--nav)}
  .social-dot.alt{background:#b23a3a}
  .brand{position:absolute;top:22px;left:0;width:816px;text-align:center;color:#5d6470}
  .brand-mark{width:38px;height:38px;border-radius:50%;background:var(--nav);margin:0 auto 14px}
  .brand-name{font-family:"Josefin Sans",sans-serif;font-weight:300;font-size:17px;letter-spacing:4px}
  .brand-sub{font-family:"Josefin Sans",sans-serif;font-weight:300;font-size:8px;letter-spacing:4px;margin-top:3px}
  .hero-name{position:absolute;top:180px;left:0;width:816px;text-align:center;font-family:"Dancing Script",cursive;font-weight:600;font-size:45px;color:var(--lime)}
  .hero-title{position:absolute;top:249px;left:0;width:816px;text-align:center;font-weight:500;font-size:15.5px;color:var(--white)}

  .main-nav{position:absolute;top:349px;left:0;width:816px;height:39px;background:var(--nav)}
  .main-nav a{position:absolute;top:11px;transform:translateX(-50%);font-family:"Noto Serif",serif;font-size:12.5px;color:var(--white);text-decoration:none;white-space:nowrap}

  .welcome{position:absolute;top:388px;left:0;width:816px;height:321px;background:var(--paper)}
  .welcome h1{position:absolute;left:29px;top:34px;font-family:"Josefin Sans",sans-serif;font-weight:300;font-size:29px;color:var(--ink)}
  .welcome .rule{position:absolute;left:29px;top:75px;width:534px;height:1px;background:#8a8a8a}
  .welcome .copy{position:absolute;left:31px;top:93px;width:530px;font-family:"Neuton",serif;font-size:11px;line-height:13.2px;color:var(--ink)}
  .welcome .copy p{margin-bottom:13px}
  .btn{display:flex;align-items:center;justify-content:center;background:var(--sky);color:var(--white);font-family:"Noto Serif",serif;font-size:11px}
  .welcome .read-more{position:absolute;left:33px;top:262px;width:93px;height:31px}
  .portrait-frame{position:absolute;left:596px;top:86px;width:187px;height:153px;background:var(--white);border:1px solid #dcdcdc;padding:4px}
  .portrait{width:100%;height:100%;background:linear-gradient(135deg,#d8b864 0%,#c9a450 45%,#9b7a3c 100%)}

  .contact{position:absolute;top:709px;left:0;width:816px;height:343px;
    background:linear-gradient(90deg,#0f110c 0%,#1a1b16 45%,#3a3a32 75%,#4a4840 100%)}
  .contact h2{position:absolute;top:29px;left:0;width:758px;text-align:center;font-family:"Josefin Sans",sans-serif;font-weight:300;font-size:38px;color:var(--lime)}
  .contact .lead{position:absolute;top:84px;left:36px;width:688px;text-align:center;font-size:11px;line-height:16px;color:var(--white)}
  .field{position:absolute;background:var(--white);font-size:9px;color:#9a9a9a;padding:10px 8px 0}
  .field.name{left:109px;top:156px;width:259px;height:28px;padding-top:9px}
  .field.email{left:109px;top:196px;width:259px;height:28px;padding-top:9px}
  .field.query{left:392px;top:156px;width:258px;height:67px;padding-top:7px}
  .contact .send{position:absolute;left:311px;top:255px;width:135px;height:34px}

  .site-footer{position:absolute;top:1052px;left:0;width:816px;height:113px;background:var(--footer)}
  .footer-col{position:absolute;top:23px}
  .footer-col h3{font-family:"Noto Serif",serif;font-weight:400;font-size:10px;color:var(--footer-head);margin-bottom:10px}
  .footer-col li{list-style:none;font-size:8.3px;color:var(--white);line-height:16px}
  .newsletter{position:absolute;left:411px;top:43px;display:flex}
  .newsletter .input{width:152px;height:22px;background:var(--white);font-size:8.3px;color:#9a9a9a;padding:6px 7px}
  .newsletter .submit{width:55px;height:22px;background:#c5e28c;font-size:9px;color:#2d3811;display:flex;align-items:center;justify-content:center}
  .follow{position:absolute;left:667px;top:41px;display:flex;gap:9px}
  .follow .social-dot{width:26px;height:26px}
  .copyright{position:absolute;top:1165px;left:0;width:816px;height:35px;background:var(--footer-dark);text-align:center;font-size:8.5px;line-height:35px;color:var(--white)}
  .copyright span{color:var(--footer-link)}
</style>
</head>
<body>
<div class="page">
  <header class="hero" role="img" aria-label="Misty shoreline with smooth rounded stones at the water's edge">
    <div class="social-top">
      <span class="social-dot" aria-label="Social profile link"></span>
      <span class="social-dot alt" aria-label="Social profile link"></span>
    </div>
    <div class="brand">
      <div class="brand-mark"></div>
      <div class="brand-name">STILLBROOK</div>
      <div class="brand-sub">WELLNESS</div>
    </div>
    <div class="hero-name">Rosalind Vantreece</div>
    <div class="hero-title">LCSW, REGISTERED PLAY THERAPIST</div>
  </header>

  <nav class="main-nav">
    <a style="left:128px">Home</a>
    <a style="left:227px">About Me</a>
    <a style="left:363px">Counseling Services</a>
    <a style="left:484px">Fees</a>
    <a style="left:565px">FAQs</a>
    <a style="left:664px">Contact Me</a>
  </nav>

  <section class="welcome">
    <h1>Rosalind Vantreece Welcomes You</h1>
    <div class="rule"></div>
    <div class="copy">
      <p>Duis gravida rhoncus enim vitae porttitor. Vivamus eget massa venenatis, aliquet mi vel, pellentesque ligula. Fusce sed massa sed orci condimentum efficitur in sit amet orci. Duis condimentum dolor eu sapien tempus dignissim. Nam elementum urna et erat luctus aliquam. Phasellus ut fringilla arcu, et dignissim lacus. Nulla facilisi. Mauris id nisi purus.</p>
      <p>Morbi ultrices tincidunt mauris in cursus. Phasellus vitae posuere justo. Nulla interdum elit quis nulla bibendum, at vulputate magna faucibus. Mauris tristique, nisi nec rutrum aliquet, nisl urna dignissim orci, ut cursus urna neque eu dolor.</p>
      <p>Aliquam quis elit risus. Donec finibus nisl sit amet finibus pulvinar. Nulla dignissim, neque ac tincidunt imperdiet, leo libero pellentesque leo, quis porta augue purus eget nunc. Cras vitae massa massa. Donec ultrices, turpis sit amet blandit ultrices, lectus metus lobortis mi, eget sodales lorem massa finibus dolor.</p>
    </div>
    <div class="btn read-more">Read More</div>
    <div class="portrait-frame">
      <div class="portrait" role="img" aria-label="Portrait photo of the therapist"></div>
    </div>
  </section>

  <section class="contact" role="img" aria-label="Dark sepia photo of wet river stones">
    <h2>I'm Here To Help You.</h2>
    <p class="lead">If you have any queries on online presence and online store management and other web related things please send us mail with a brief of your question.</p>
    <div class="field name">Your Name</div>
    <div class="field email">Your Email id</div>
    <div class="field query">Your Queries</div>
    <div class="btn send">Send</div>
  </section>

  <footer class="site-footer">
    <div class="footer-col" style="left:22px"><h3>About</h3><ul><li>Who I Am</li><li>Specialties</li><li>Approach</li></ul></div>
    <div class="footer-col" style="left:113px"><h3>Counselling Services</h3><ul><li>Individual Counseling</li><li>Play Therapy</li><li>Sandplay Therap</li></ul></div>
    <div class="footer-col" style="left:260px"><h3>Latest Posts</h3><ul><li>Lorem ipsumm dolor sit</li><li>Nuno valencia esdt di</li><li>Di maria nuno estelem</li></ul></div>
    <div class="footer-col" style="left:408px"><h3>Subscribe Newsletter</h3></div>
    <div class="newsletter"><div class="input">Your Email id</div><div class="submit">Submit</div></div>
    <div class="footer-col" style="left:667px"><h3>Follow Me</h3></div>
    <div class="follow">
      <span class="social-dot" aria-label="Social profile link"></span>
      <span class="social-dot" style="background:var(--sky)" aria-label="Social profile link"></span>
      <span class="social-dot alt" aria-label="Social profile link"></span>
    </div>
  </footer>
  <div class="copyright">Rosalind Vantreece© 2016 Copyright &nbsp;|&nbsp; <span>Make an enquiry</span> &nbsp;|&nbsp; <span>Privacy statement.</span></div>
</div>
</body>
</html>
```